Refrigerated trailer business needs an email flyer

We need an email flyer for mass distribution to potential customers. We are marketing to anyone who has/uses walk-in coolers & freezers and may need a refrigerated trailer for emergency or overflow needs. Our target customers are: school systems, restaurants, universities, caterers, event organizers, etc.
Possible wording:
We Get it!!

Frostline Haulage Storage, LLC is a mobile refrigerated trailer rental company. We have more than 40 years of experience servicing commercial refrigeration systems so we understand the importance of protecting your refrigerated inventory while controlling cost so your business continues to run smoothly. We’ve seen schools and restaurants scramble to find a way to save their refrigerated and frozen food when a walk-in goes down and parts aren’t readily available. We have watched our customers with seasonal business spikes (Mother’s Day, Valentine’s Day, etc.) struggle to find extra space for their refrigerated products. We know the struggles that vendors have trying to find on-site refrigerated storage for special events. We are here to help meet these needs so you can focus on your customers.

Possible Tagline: Cold storage when you need it, where you need it.
Units work as Coolers or Freezers. Works on a 115v dedicated circuit.
www.brisklockunits.com
(555)207-3916

```html
<!DOCTYPE html>
<html lang="en">
<head>
<meta charset="utf-8">
<title>Frostline Haulage Storage – Cold Storage Flyer</title>
<link rel="stylesheet" href="https://fonts.googleapis.com/css2?family=Montserrat:wght@600;700;800&family=Questrial&display=swap">
<style>
  :root {
    --navy: #1f3a78;
    --navy-deep: #14285a;
    --blue: #1d78c8;
    --blue-bright: #2b8fe0;
    --ink: #20386f;
    --white: #ffffff;
    --paper: #f4f5f7;
    --silver: #e4e6ea;
    --heading: "Montserrat", Arial, sans-serif;
    --body: "Questrial", "Century Gothic", sans-serif;
  }
  * { box-sizing: border-box; margin: 0; padding: 0; }
  html, body { width: 914px; height: 1200px; overflow: hidden; background: var(--white); }
  .flyer { position: relative; width: 914px; height: 1200px; overflow: hidden; background: linear-gradient(180deg, var(--white) 60%, var(--paper)); font-family: var(--body); color: var(--ink); }

  .hero-backdrop { position: absolute; inset: 0 0 auto 0; height: 780px;
    background: radial-gradient(ellipse at 45% 35%, #2c4f96 0%, #1d3a7a 45%, #142a5e 100%); }
  .hero-cut { position: absolute; left: 0; top: 0; width: 914px; height: 1200px; }

  .headline { position: absolute; top: 40px; width: 100%; text-align: center; }
  .headline h1 { font-family: var(--heading); font-weight: 700; font-size: 60px; letter-spacing: 1px; line-height: 1;
    color: #f1f2f4; text-shadow: 0 2px 4px rgba(0,0,0,.35); }
  .tagline { display: inline-block; margin-top: 10px; width: 554px; height: 34px; line-height: 34px; border-radius: 17px;
    background: linear-gradient(90deg, #1566b8, var(--blue-bright) 50%, #1566b8);
    font-family: var(--heading); font-weight: 700; font-size: 20px; color: var(--white); letter-spacing: .3px; }
  .specs { margin-top: 12px; font-size: 23px; line-height: 29px; color: var(--white); }

  .trailer-photo { position: absolute; left: 77px; top: 277px; width: 746px; height: 503px; border-radius: 24px;
    background: radial-gradient(ellipse at 55% 45%, #fbfbfc 0%, #e6e8ec 55%, rgba(210,215,225,.0) 78%); }

  .about { position: absolute; left: 55px; top: 800px; width: 380px; }
  .about h2 { font-family: var(--heading); font-weight: 800; font-size: 40px; line-height: 1; color: var(--blue); letter-spacing: -.5px; }
  .about p { margin-top: 8px; font-size: 14.6px; line-height: 17.2px; color: var(--ink); }

  .gallery { position: absolute; left: 470px; top: 814px; width: 400px; height: 184px; }
  .gallery-frame { position: absolute; left: 0; top: 40px; width: 400px; height: 132px; border: 1px solid #9aa3b4; }
  .gallery-frame::before, .gallery-frame::after { content: ""; position: absolute; top: -2px; bottom: -2px; background: var(--white); }
  .gallery-frame::before { left: 23px; right: 23px; top: -2px; height: 4px; }
  .gallery-frame::after { left: 27px; right: 27px; top: auto; bottom: -2px; height: 4px; }
  .shot { position: absolute; top: 0; width: 112px; height: 138px; }
  .shot-step { left: 24px; background: linear-gradient(180deg, #b8c2cc 0%, #3f78c2 32%, #8c9096 45%, #5f6368 100%); }
  .shot-door { left: 147px; background: linear-gradient(180deg, #3f8ee0 0%, #8fb8e6 30%, #e9ecef 45%, #a59f95 100%); }
  .shot-inside { left: 271px; background: linear-gradient(180deg, #f3f3f1 0%, #e6e5e1 60%, #6b6e72 75%, #5b5e62 100%); }
  .shot-label { position: absolute; top: 165px; width: 112px; text-align: center; font-size: 16px; color: var(--blue); background: var(--white); }

  .promise { position: absolute; left: 55px; top: 1030px; width: 815px; height: 31px; border: 1.5px solid var(--blue); border-radius: 16px;
    text-align: center; line-height: 28px; font-family: var(--heading); font-weight: 700; font-size: 16.5px; color: var(--blue); }

  .contact-band { position: absolute; left: 0; top: 1088px; width: 560px; height: 91px; background: var(--navy);
    border-radius: 0 46px 46px 0; color: var(--white); padding: 14px 0 0 56px; }
  .contact-band .call { font-size: 29px; line-height: 34px; }
  .contact-band .call strong { font-family: var(--heading); font-weight: 800; }
  .contact-band .web { font-size: 20px; line-height: 24px; margin-left: 2px; }

  .brand { position: absolute; left: 575px; top: 1102px; width: 300px; text-align: center; font-family: var(--heading); font-weight: 800; color: var(--navy); }
  .brand .brand-main { display: block; font-size: 34px; line-height: 36px; letter-spacing: 1px; }
  .brand .brand-sub { display: block; font-size: 16px; line-height: 22px; letter-spacing: 2.2px; }
</style>
</head>
<body>
<main class="flyer">
  <div class="hero-backdrop" role="img" aria-label="Blurred navy-toned photo of frozen food being handled in cold storage"></div>
  <svg class="hero-cut" viewBox="0 0 914 1200" aria-hidden="true">
    <polygon points="0,740 914,548 914,1200 0,1200" fill="#ffffff"/>
    <polygon points="780,650 914,628 914,592 790,615" fill="#1d78c8"/>
    <polygon points="0,776 330,706 330,712 0,782" fill="#1d78c8"/>
  </svg>

  <header class="headline">
    <h1>COLD STORAGE</h1>
    <div class="tagline">WHEN YOU NEED IT, WHERE YOU NEED IT.</div>
    <p class="specs">Units work as Coolers or Freezers.<br>Works on a 115v dedicated circuit.</p>
  </header>

  <div class="trailer-photo" role="img" aria-label="Photo of a white refrigerated rental trailer on a blue tandem-axle chassis with the company name on its side"></div>

  <section class="about">
    <h2>WE GET IT!!</h2>
    <p>Frostline Haulage Storage, LLC is a mobile refrigerated trailer rental company. We have more than 40 years of experience servicing commercial refrigeration systems so we understand the importance of protecting your refrigerated inventory while controlling cost so your business continues to run smoothly.</p>
  </section>

  <section class="gallery">
    <div class="gallery-frame"></div>
    <div class="shot shot-step" role="img" aria-label="Photo of the trailer's fold-down rear step over gravel"></div>
    <div class="shot shot-door" role="img" aria-label="Photo of the trailer's open back door with strip curtain"></div>
    <div class="shot shot-inside" role="img" aria-label="Photo of the white insulated interior of the trailer"></div>
    <span class="shot-label" style="left:24px">Step</span>
    <span class="shot-label" style="left:147px">Back Door</span>
    <span class="shot-label" style="left:271px">Inside</span>
  </section>

  <p class="promise">We are here to help meet these needs so you can focus on your customers.</p>

  <footer>
    <div class="contact-band">
      <p class="call">Call us <strong>555-207-3916</strong></p>
      <p class="web">www.brisklockunits.com</p>
    </div>
    <p class="brand"><span class="brand-main">FROSTLINE</span><span class="brand-sub">HAULAGE STORAGE</span></p>
  </footer>
</main>
</body>
</html>
```